VORDA HOMES PELAB MARKETING FLYER

THE FLYER CAN BE FRONT TO BACK OR 2 PAGES IF NEEDED.

need to create a flyer with the following information:

Tallyworth Inc. is a CRM (Customer Relationship Management System) that provides leads to agents and a system to communicate and track your leads. Initial training and set up will be provided

Commission splits for leads are as follows: (maybe we can create a chart or box for items 1-3)

1. Cold leads 40% Vorda - 60% Agent - Worked by Agent in the platform, agent shows property, writes contract, handles all negotiations and any necessary addendums, attends home inspection and settlement.

2. Warm leads 50% Vorda - 50% Co-agent - Contacted by ISA, agent shows property, writes contract, handles all negotiations and any necessary addendums, attends home inspection and settlement.

3 Hot leads 70% Vorda - 30% Co-agent - Prequalified by Vorda Homes and ready to look at property, Vorda writes contract and secures broker agency relationship agreements, co-agent shows property, , handles all negotiations (with support from VORDA if necessary), execute any necessary addendums, attend home inspection and settlement.

Preferred vendors such as Lender, Title, Insurance, Home Inspector, etc. are to be used for any transactions related to PELB per Vorda Homes.

Agents will receive 10 leads for free to start once Fresh Broker Launchpad is complete. Warm leads will be available to purchase for $15 each beyond the first 10. Every 5 deals closed, agent commission will increase by 10% annually!!

Rules and restrictions apply.

3. In addition to Quillset, a transaction coordinator included.

4. Free PELB Support and training included

5. Free personal CRM website included

Industry/Entity Type

Real Estate

Colors
3176b5
85abd2
ecf5f6

Requirements
Must have
• everything in the description above

```html
<!DOCTYPE html>
<html lang="en">
<head>
<meta charset="utf-8">
<title>Vorda Homes – Tallyworth Inc. Flyer</title>
<link href="https://fonts.googleapis.com/css2?family=Anton&family=Montserrat:wght@300;400;600;700;800&display=swap" rel="stylesheet">
<style>
  :root {
    --brand-blue: #3176b5;
    --deep-blue: #1f5fa8;
    --soft-blue: #85abd2;
    --mist: #ecf5f6;
    --ink: #3a3a3a;
    --body-ink: #555555;
    --strip-light: #8a8a8a;
    --strip-dark: #6d6d6d;
    --number-grey: #b9b9b9;
    --page-bg: #dcdcdc;
    --paper: #ffffff;
  }
  * { box-sizing: border-box; margin: 0; padding: 0; }
  html, body { width: 1200px; height: 2390px; overflow: hidden; }
  body { background: var(--page-bg); font-family: "Montserrat", sans-serif; position: relative; }

  .flyer {
    position: absolute; left: 0; top: 346px; width: 1200px; height: 1697px;
    background: var(--paper); box-shadow: 0 6px 24px rgba(0,0,0,.25); overflow: hidden;
  }
  .flyer > * { position: absolute; }

  .brand-mark { color: var(--deep-blue); font-weight: 700; white-space: nowrap; }
  .brand-primary { left: 104px; top: 118px; font-size: 34px; letter-spacing: 1px;
    display: flex; align-items: center; gap: 16px; }
  .brand-primary .square { width: 32px; height: 32px; background: currentColor; display: block; }
  .brand-partner { left: 470px; top: 96px; width: 240px; font-size: 22px; font-weight: 400;
    color: var(--brand-blue); display: flex; flex-direction: column; align-items: center; gap: 14px; }
  .brand-partner .square { width: 30px; height: 30px; background: currentColor; display: block; }

  .frame-top { left: 748px; top: 136px; width: 439px; height: 11px; background: var(--brand-blue); }
  .frame-side { left: 1176px; top: 136px; width: 11px; height: 732px; background: var(--brand-blue); }

  .photo { display: block; }
  .photo-house { left: 555px; top: 239px; width: 611px; height: 488px;
    background: linear-gradient(180deg, #cfdde6 0%, #8e9aa6 30%, #4f5a44 55%, #4e8f2c 72%, #6fae3a 100%); }
  .photo-pool { left: 90px; top: 627px; width: 438px; height: 283px; z-index: 2;
    background: linear-gradient(180deg, #e9ecee 0%, #c7b9a6 35%, #6fa852 55%, #5fb8c2 75%, #7fd0d6 100%); }
  .photo-framed { top: 925px; height: 262px; border: 5px solid #fff; box-shadow: 0 2px 8px rgba(0,0,0,.3); }
  .photo-villa { left: 87px; width: 244px;
    background: linear-gradient(180deg, #bcd6ee 0%, #e8e2da 45%, #7a7470 60%, #69c3cf 100%); }
  .photo-family { left: 337px; width: 233px;
    background: linear-gradient(180deg, #e7e5e2 0%, #b9a493 45%, #4b5866 80%, #2e3640 100%); }

  .headline { left: 87px; top: 280px; font-family: "Anton", sans-serif; line-height: 1; }
  .headline .lead { color: var(--brand-blue); font-size: 58px; display: block; margin-bottom: 8px; }
  .headline .line { color: var(--ink); font-size: 76px; display: block; margin-bottom: 2px; letter-spacing: -0.5px; }

  .band-left { left: 0; top: 757px; width: 90px; height: 156px; background: var(--brand-blue); }
  .band-right { left: 534px; top: 757px; width: 666px; height: 156px; background: var(--brand-blue);
    color: #fff; padding: 26px 50px 0 52px; font-size: 20px; line-height: 24px; }
  .band-right strong { font-weight: 700; }

  .splits { left: 612px; top: 925px; width: 480px; }
  .splits-title { font-size: 29px; line-height: 35px; color: var(--ink); font-weight: 700; }
  .splits-title span { display: block; font-weight: 300; letter-spacing: 1px; }
  .splits-rule { width: 134px; height: 5px; background: var(--brand-blue); margin: 6px 0 22px; }
  .split-item { display: flex; gap: 10px; margin-bottom: 22px; font-size: 15.5px; line-height: 19.5px; color: var(--body-ink); text-align: justify; }
  .split-item svg { flex: none; width: 22px; height: 22px; margin-top: 1px; }
  .split-item b { color: var(--brand-blue); font-weight: 700; }

  .vendors { left: 85px; top: 1227px; width: 470px; font-size: 16px; line-height: 19.5px; color: var(--body-ink); text-align: justify; }
  .vendors b { color: var(--ink); }

  .rules-tab { left: 291px; top: 1378px; width: 616px; height: 60px; background: var(--deep-blue);
    border-radius: 14px 14px 0 0; color: #fff; font-weight: 700; font-size: 29px; text-align: center; line-height: 64px; }

  .perks { left: 0; top: 1437px; width: 1200px; height: 147px; display: flex; }
  .perk { display: flex; align-items: center; gap: 14px; padding-left: 46px; color: #fff; font-weight: 700; font-size: 19px; line-height: 23px; }
  .perk:nth-child(1) { width: 407px; background: var(--strip-light); }
  .perk:nth-child(2) { width: 393px; background: var(--strip-dark); padding-left: 16px; }
  .perk:nth-child(3) { width: 400px; background: var(--strip-light); padding-left: 16px; }
  .perk-number { font-size: 62px; font-weight: 800; color: var(--number-grey); line-height: 1; }

  .web-address { left: 0; top: 1620px; width: 1200px; text-align: center; font-size: 24px; font-weight: 700; letter-spacing: 5px; color: var(--ink); }
</style>
</head>
<body>
<main class="flyer">
  <div class="brand-mark brand-primary"><span class="square"></span>VORDA HOMES</div>
  <div class="brand-mark brand-partner"><span class="square"></span>Harbor Lane Group</div>

  <div class="frame-top"></div>
  <div class="frame-side"></div>

  <div class="photo photo-house" role="img" aria-label="Photo of a suburban home at dusk with lit windows and a green lawn"></div>

  <h1 class="headline">
    <span class="lead">TALLYWORTH INC.</span>
    <span class="line">RELATIONSHIP</span>
    <span class="line">MANAGEMENT</span>
    <span class="line">SYSTEM</span>
  </h1>

  <div class="band-left"></div>
  <div class="photo photo-pool" role="img" aria-label="Photo of a modern villa terrace with a swimming pool and umbrella"></div>
  <p class="band-right"><strong>Tallyworth Inc. is a CRM (Customer Relationship Management System)</strong> that provides leads to agents and a system to communicate and track your leads. Initial training and set up will be provided</p>

  <div class="photo photo-framed photo-villa" role="img" aria-label="Photo of a poolside villa with patio furniture"></div>
  <div class="photo photo-framed photo-family" role="img" aria-label="Photo of a family sitting under a cardboard roof shape"></div>

  <section class="splits">
    <h2 class="splits-title">COMMISSION SPLITS FOR<span>LEADS ARE AS FOLLOWS</span></h2>
    <div class="splits-rule"></div>
    <div class="split-item">
      <svg viewBox="0 0 24 24" fill="none" stroke="#3176b5" stroke-width="2"><circle cx="12" cy="12" r="9.5"/><path d="M7.5 12.5l3 3 6.5-7"/></svg>
      <p><b>Cold leads 40% Vorda - 60% Agent -</b> Worked by Agent in the platform, agent shows property, writes contract, handles all negotiations and any necessary addendums, attends home inspection and settlement.</p>
    </div>
    <div class="split-item">
      <svg viewBox="0 0 24 24" fill="none" stroke="#3176b5" stroke-width="2"><circle cx="12" cy="12" r="9.5"/><path d="M7.5 12.5l3 3 6.5-7"/></svg>
      <p><b>Warm leads 50% Vorda - 50% Co-agent -</b> Contacted by ISA, agent shows property, writes contract, handles all negotiations and any necessary addendums, attends home inspection and settlement.</p>
    </div>
    <div class="split-item">
      <svg viewBox="0 0 24 24" fill="none" stroke="#3176b5" stroke-width="2"><circle cx="12" cy="12" r="9.5"/><path d="M7.5 12.5l3 3 6.5-7"/></svg>
      <p><b>Hot leads 70% Vorda - 30% Co-agent -</b> Prequalified by Vorda Homes and ready to look at property, Vorda writes contract and secures broker agency relationship agreements, co-agent shows property, handles all negotiations (with support from VORDA if necessary), execute any necessary addendums, attend home inspection and settlement.</p>
    </div>
  </section>

  <p class="vendors">Preferred vendors such as Lender, Title, Insurance, Home Inspector, etc. are to be used for any transactions related to <b>PELB</b> per Vorda Homes. Agents will receive 10 leads for free to start once Fresh Broker Launchpad is complete. Warm leads will be available to purchase for $15 each beyond the first 10. Every 5 deals closed, agent commission will <b>increase by 10% annually!!</b></p>

  <div class="rules-tab">RULES AND RESTRICTIONS APPLY</div>

  <div class="perks">
    <div class="perk"><span class="perk-number">01</span><span>In addition to Quillset,<br>a transaction coordinator<br>included.</span></div>
    <div class="perk"><span class="perk-number">02</span><span>Free PELB Support and<br>training included</span></div>
    <div class="perk"><span class="perk-number">03</span><span>Free personal CRM<br>website included</span></div>
  </div>

  <p class="web-address">www.vordahomes.net</p>
</main>
</body>
</html>
```